Business Card Design job - Tessa's Business Cards

Simple elegant feminine design - Going out on my own as a Mortgage Broker.
My thoughts are the following details on the Front, middle of the card possibly? Phone and email smaller font than my name?
Tessa Marwick
Finance Specialist
p: 0438 217 905
e: tessa@marwickfinance.com.au
Bottom of the card
residential / commercial / equipment
I would like the Font in Rose Gold maybe white or black background? or Possibly a stone grey - are you able to do a few options? I'd like them embossed
Then I had an idea as a simple logo as per the attached if you get the idea in my scribble, my initials, capital T attached to a small m that leads/follows into a circle? Thicker Font In Rose Gold, middle of the card at the back.
Very open to ideas though and what colour you think would look better with the Rose Gold.
Thanks so much for your help, I am not very creative and savvy with this stuff :-)
Industry/Entity Type
Finance
Contact Information for Business Card
Tessa Marwick
p: 0438 217 905
Look and feel
Each slider illustrates characteristics of the customer's brand and the style your logo design should communicate.

```html
<!DOCTYPE html>
<html lang="en">
<head>
<meta charset="utf-8">
<title>Tessa Marwick — Business Cards</title>
<link rel="stylesheet" href="https://fonts.googleapis.com/css2?family=Poiret+One&display=swap">
<style>
  :root {
    --backdrop: #ffffff;
    --paper: #eff1ee;
    --paper-edge: #e2e5e1;
    --rose-gold: #d5866a;
    --rose-gold-deep: #c06e54;
  }
  * { box-sizing: border-box; margin: 0; padding: 0; }
  html, body {
    width: 1200px;
    height: 1000px;
    overflow: hidden;
    background: var(--backdrop);
  }
  .canvas {
    position: relative;
    width: 1200px;
    height: 1000px;
    font-family: "Poiret One", sans-serif;
    color: var(--rose-gold);
  }
  .card {
    position: absolute;
    left: 290px;
    width: 620px;
    height: 352px;
    background: var(--paper);
    border: 1px solid var(--paper-edge);
  }
  .card--front { top: 145px; }
  .card--back  { top: 520px; }

  /* Front: brand name in place of the monogram */
  .brand {
    position: absolute;
    inset: 0;
    display: flex;
    align-items: center;
    justify-content: center;
    gap: 16px;
  }
  .brand__dot {
    width: 14px;
    height: 14px;
    border-radius: 50%;
    background: var(--rose-gold);
  }
  .brand__name {
    font-size: 34px;
    letter-spacing: 5px;
    text-transform: uppercase;
    color: var(--rose-gold);
  }

  /* Back: contact details */
  .details {
    position: absolute;
    top: 88px;
    left: 0;
    right: 0;
    text-align: center;
    text-transform: uppercase;
  }
  .details__name {
    display: inline-block;
    font-size: 31px;
    letter-spacing: 3px;
    line-height: 1;
    padding: 0 2px 3px;
    border-bottom: 1.5px solid var(--rose-gold-deep);
    color: var(--rose-gold-deep);
  }
  .details__role {
    margin-top: 8px;
    font-size: 13px;
    letter-spacing: 2px;
  }
  .details__contact {
    margin-top: 48px;
    font-size: 15px;
    letter-spacing: 1.5px;
    line-height: 18px;
    color: var(--rose-gold-deep);
  }
  .divider {
    position: absolute;
    left: 47px;
    right: 44px;
    top: 282px;
    height: 2px;
    background: var(--rose-gold);
  }
  .services {
    position: absolute;
    top: 306px;
    left: 0;
    right: 0;
    text-align: center;
    text-transform: uppercase;
    font-size: 15px;
    letter-spacing: 2px;
    word-spacing: 4px;
    color: var(--rose-gold-deep);
  }
</style>
</head>
<body>
  <main class="canvas">
    <section class="card card--front" aria-label="Card front">
      <div class="brand">
        <span class="brand__dot" aria-hidden="true"></span>
        <span class="brand__name">Marwick Finance</span>
      </div>
    </section>

    <section class="card card--back" aria-label="Card back">
      <div class="details">
        <h1 class="details__name">Tessa Marwick</h1>
        <p class="details__role">Finance Specialist</p>
        <p class="details__contact">
          Phone : 0438 217 905<br>
          Email : tessa@marwickfinance.com.au
        </p>
      </div>
      <div class="divider" aria-hidden="true"></div>
      <p class="services">Residential / Commercial / Equipment</p>
    </section>
  </main>
</body>
</html>
```